Business cards - KESTO Roofing & Siding

We need simple business cards made up for our Roofing & Siding business based in Calgary Alberta.
The logo on one side of the card and potentially our slogan "Built with trust, verified by time".
The other side could have:
-A small logo
-Rep name:
-Rep cell phone:
-Rep email:
-Office phone: 403-386-2049
-Website: PrairieShinglePros.com

We would like to incorporate the colours from our logo, especially the lite blue on the jpeg file. I have attached the ai file and jpeg file. We like the colours better on the jpeg file.

I do not require a money back guarantee

```html
<!DOCTYPE html>
<html lang="en">
<head>
<meta charset="utf-8">
<title>KESTO Roofing &amp; Siding — Business Cards</title>
<link rel="stylesheet" href="https://fonts.googleapis.com/css2?family=Arimo:wght@400;700&family=Michroma&display=swap">
<style>
  :root {
    --backdrop: #e6e6e4;
    --card: #393939;
    --card-dark: #2a2a2a;
    --ink: #ffffff;
    --accent-red: #e5262b;
    --accent-blue: #4a8fd6;
    --rule: #d8d8d8;
    --panel-light: #5a5a5a;
    --panel-dark: #222222;
  }
  * { box-sizing: border-box; margin: 0; padding: 0; }
  html, body { width: 1200px; height: 801px; overflow: hidden; }
  body {
    background: var(--backdrop);
    font-family: "Arimo", Arial, sans-serif;
    color: var(--ink);
    position: relative;
  }
  .card {
    position: absolute;
    top: 252px;
    width: 520px;
    height: 297px;
    background: var(--card);
    border-radius: 3px;
    box-shadow: 0 6px 18px rgba(0,0,0,0.25);
    overflow: hidden;
  }
  .card--front { left: 50px; }
  .card--back  { left: 630px; }

  /* Brand block */
  .brand { position: absolute; }
  .brand__est {
    font-family: "Michroma", sans-serif;
    font-size: 9px;
    letter-spacing: 1.5px;
    display: block;
    margin-bottom: 4px;
  }
  .brand__row { display: flex; align-items: center; gap: 8px; }
  .brand__mark {
    width: 14px; height: 14px;
    background: var(--accent-blue);
  }
  .brand__name {
    font-family: "Arimo", Arial, sans-serif;
    font-weight: 700;
    font-size: 42px;
    letter-spacing: 4px;
    line-height: 1;
    color: var(--ink);
  }
  .brand__tag {
    font-family: "Michroma", sans-serif;
    font-size: 11.5px;
    letter-spacing: 3px;
    display: block;
    margin-top: 6px;
  }
  .card--front .brand { left: 36px; top: 50px; }
  .card--back .brand { right: 34px; top: 44px; }

  /* Rep */
  .rep { position: absolute; left: 36px; top: 196px; }
  .rep__name {
    color: var(--accent-red);
    font-size: 17px;
    font-weight: 400;
    letter-spacing: 0.5px;
  }
  .rep__title { font-size: 14px; margin-top: 4px; }

  .divider {
    position: absolute;
    left: 268px; top: 150px;
    width: 1px; height: 100px;
    background: var(--rule);
  }

  /* Contacts */
  .contacts {
    position: absolute;
    left: 290px; top: 142px;
    list-style: none;
  }
  .contacts__item {
    display: flex; align-items: center; gap: 10px;
    font-size: 14px;
    height: 28px;
  }
  .contacts__icon { width: 14px; height: 14px; flex: none; }

  /* Back artwork area */
  .back-artwork {
    position: absolute;
    left: 0; bottom: 0;
    width: 100%; height: 150px;
    background: linear-gradient(90deg, var(--panel-dark) 0%, var(--card-dark) 50%, var(--panel-light) 100%);
  }
</style>
</head>
<body>

  <section class="card card--front" aria-label="Business card, contact side">
    <div class="brand">
      <span class="brand__est">Est. 1991</span>
      <div class="brand__row">
        <span class="brand__mark"></span>
        <span class="brand__name">KESTO</span>
      </div>
      <span class="brand__tag">ROOFING &amp; SIDING</span>
    </div>

    <div class="rep">
      <p class="rep__name">DANIEL MORROW</p>
      <p class="rep__title">Manager</p>
    </div>

    <span class="divider"></span>

    <ul class="contacts">
      <li class="contacts__item">
        <svg class="contacts__icon" viewBox="0 0 14 14" aria-hidden="true"><rect x="3.5" y="1" width="7" height="12" rx="1.2" fill="none" stroke="var(--accent-red)" stroke-width="1.5"/><circle cx="7" cy="11" r="0.8" fill="var(--accent-red)"/></svg>
        <span>403-386-2049</span>
      </li>
      <li class="contacts__item">
        <svg class="contacts__icon" viewBox="0 0 14 14" aria-hidden="true"><path d="M3 1.5l2.5 0 1 3-1.5 1.2a7 7 0 0 0 3.3 3.3l1.2-1.5 3 1v2.5a1.5 1.5 0 0 1-1.5 1.5A10.5 10.5 0 0 1 1.5 3 1.5 1.5 0 0 1 3 1.5z" fill="var(--accent-red)"/></svg>
        <span>403-386-2049</span>
      </li>
      <li class="contacts__item">
        <svg class="contacts__icon" viewBox="0 0 14 14" aria-hidden="true"><rect x="1" y="3" width="12" height="8.5" fill="var(--accent-red)"/><path d="M1 3l6 5 6-5" fill="none" stroke="var(--card)" stroke-width="1.2"/></svg>
        <span>info@PrairieShinglePros.com</span>
      </li>
      <li class="contacts__item">
        <svg class="contacts__icon" viewBox="0 0 14 14" aria-hidden="true"><circle cx="7" cy="7" r="6" fill="var(--accent-red)"/><path d="M1 7h12M7 1c-3 3-3 9 0 12M7 1c3 3 3 9 0 12" fill="none" stroke="var(--card)" stroke-width="1"/></svg>
        <span>PrairieShinglePros.com</span>
      </li>
    </ul>
  </section>

  <section class="card card--back" aria-label="Business card, brand side">
    <div class="brand">
      <span class="brand__est">Est. 1991</span>
      <div class="brand__row">
        <span class="brand__name">KESTO</span>
      </div>
      <span class="brand__tag">ROOFING &amp; SIDING</span>
    </div>
    <div class="back-artwork" role="img" aria-label="Decorative house artwork with windows and a red leaf"></div>
  </section>

</body>
</html>
```